A4 Single Page Brochure for Private Cloud Offerings

Theme: Futuristic Tech Company

Brightmoor Systems is looking to offer private cloud services for our enterprise customers in Perth-based data-centres that provides our clients with a lower-cost alternative to Nimbra or KLT yielding better performance.

We are looking for a single A4 brochure with a great graphics design theme to promote these services.

We will be providing five tiers:
- Starter
- Growth
- Professional
- Premier
- Elite

Each plan must list on the brochure the Max VMs, CPU cores, Memory and SSD storage allocated. Refer to the uploaded PNG file.

The brochure must list the following selling points:

- Hosted in a local Perth-based TIER3 and TIER4 datacentres
- WA owned hosting - support local
- Low latency - ultra fast local hosting
- Includes Quorra Host Datacentre licensing
- Includes WallHaven Managed Firewalls for Enterprise level threat detection
- Includes all infrastructure maintenance services
- Full self management of VMs through customer portal
- Includes a 1gbps Internet link
- Predictable fixed monthly fee with no dynamic billing
- No additional charges for Storage Transactions, Internet Usage, VM Snapshots, Datacentre Bandwidth Usage and Firewall Traffic Usage.
- Highly available cluster, no single point of failure.
- Pricing is based on 36 months commit
- Yearly rate increases capped to a maximum of Australian CPI
- All plans have 24/7/365 support with dedicated after hours number.
- Managed backup and managed disaster recovery services can be added to plans

Service provided in accordance with our terms and conditions.

We need the ability to EDIT the brochure to adjust pricing after we receive the final project.

Please do not utilise "Pushing the Boundaries of Technology" - our brand is being replaced with "Specialised Consulting". New website is under development but not launched yet.

Target Market(s)

Information Technology Sector

Colors
0054AA
0677BA
7BADD7
CADEEF
E8F1F8

Requirements
Must have
• Theme of Brightmoor is Blue
Should not have
• Extremely stock imagary that just looks "cheap and stock"

```html
<!DOCTYPE html>
<html lang="en">
<head>
<meta charset="utf-8">
<title>Brightmoor Systems – Private Cloud Tiers</title>
<link rel="stylesheet" href="https://fonts.googleapis.com/css2?family=Oswald:wght@300;500;600&family=Montserrat:wght@700&display=swap">
<style>
  :root {
    --blue-deep: #0054AA;
    --blue-mid: #0677BA;
    --blue-soft: #7BADD7;
    --blue-pale: #CADEEF;
    --blue-mist: #E8F1F8;
    --navy: #0a3f8f;
    --ink: #1f4fa3;
    --white: #ffffff;
  }
  * { box-sizing: border-box; margin: 0; padding: 0; }
  html, body { width: 849px; height: 1200px; overflow: hidden; background: var(--white); }
  .brochure { position: relative; width: 849px; height: 1200px; background: var(--white); overflow: hidden; font-family: 'Montserrat', sans-serif; }

  .office-backdrop {
    position: absolute; left: 0; top: 0; width: 849px; height: 520px;
    background: linear-gradient(180deg, #dfe7f1 0%, #eef3f8 55%, rgba(255,255,255,0) 100%);
  }
  .top-accent { position: absolute; left: 55px; top: 0; width: 75px; height: 7px; background: var(--blue-deep); }

  .hero-photo { position: absolute; left: 0; top: 75px; width: 600px; height: 325px; }
  .hero-stripe { position: absolute; left: 0; top: 0; width: 849px; height: 460px; }

  .headline {
    position: absolute; left: 54px; top: 146px; color: var(--white);
    font-family: 'Oswald', sans-serif; font-size: 57px; line-height: 66px; text-transform: uppercase; letter-spacing: 0.3px;
  }
  .headline .strong { font-weight: 600; display: block; }
  .headline .light { font-weight: 300; display: block; }

  .brand-name {
    position: absolute; left: 546px; top: 208px; width: 240px; text-align: center;
    font-family: 'Oswald', sans-serif; font-weight: 500; font-size: 30px; line-height: 34px;
    color: var(--navy); text-transform: uppercase; letter-spacing: 2px;
  }
  .brand-mark { display: block; width: 26px; height: 26px; margin: 0 auto 12px; background: var(--blue-deep); }

  .tiers-intro {
    position: absolute; left: 587px; top: 352px; font-family: 'Oswald', sans-serif; font-weight: 500;
    font-size: 21px; color: var(--blue-deep); text-transform: uppercase; letter-spacing: 0.3px;
  }
  .tiers-band { position: absolute; left: 488px; top: 385px; width: 361px; height: 64px; }
  .tiers-title {
    position: absolute; left: 586px; top: 387px; font-family: 'Oswald', sans-serif; font-weight: 500;
    font-size: 44px; line-height: 60px; color: var(--white); text-transform: uppercase;
  }
  .side-accent { position: absolute; left: 25px; top: 417px; width: 9px; height: 75px; background: var(--blue-deep); }
  .side-accent-light { position: absolute; left: 815px; top: 630px; width: 8px; height: 77px; background: var(--blue-mist); }

  .tier-row { position: absolute; left: 25px; top: 513px; width: 799px; height: 86px; display: flex; }
  .tier { position: relative; flex: 1; display: flex; align-items: flex-end; justify-content: center; padding-bottom: 20px;
    font-family: 'Oswald', sans-serif; font-weight: 500; font-size: 21px; text-transform: uppercase; }
  .tier-starter { background: var(--blue-deep); color: var(--white); }
  .tier-growth { background: var(--blue-mid); color: var(--white); }
  .tier-professional { background: var(--blue-soft); color: var(--white); }
  .tier-premier { background: var(--blue-pale); color: var(--blue-deep); }
  .tier-elite { background: var(--blue-mist); color: var(--blue-deep); }
  .tier-icon {
    position: absolute; left: 50%; top: -52px; width: 74px; height: 74px; margin-left: -37px;
    border-radius: 50%; background: var(--white); display: flex; align-items: center; justify-content: center;
  }
  .tier-icon svg { width: 40px; height: 40px; fill: none; stroke: var(--navy); stroke-width: 1.6; stroke-linecap: round; stroke-linejoin: round; }

  .selling-points { position: absolute; left: 58px; top: 653px; width: 770px; list-style: none; }
  .selling-points li {
    position: relative; padding-left: 24px; margin-bottom: 12.4px;
    font-weight: 700; font-size: 12.6px; line-height: 19px; color: var(--ink); text-transform: uppercase; letter-spacing: 0;
  }
  .selling-points li::before {
    content: ""; position: absolute; left: 0; top: 4px; width: 14px; height: 11px;
    background: var(--blue-soft); clip-path: polygon(0 0, 45% 0, 100% 50%, 45% 100%, 0 100%, 55% 50%);
  }

  .footer-bar { position: absolute; top: 1190px; height: 10px; }
  .footer-bar.one { left: 0; width: 139px; background: var(--blue-mid); }
  .footer-bar.two { left: 164px; width: 201px; background: var(--blue-soft); }
  .footer-bar.three { left: 385px; width: 464px; background: var(--blue-pale); }
</style>
</head>
<body>
<main class="brochure">
  <div class="office-backdrop" role="img" aria-label="Faded photo of a bright modern office in pale blue tones"></div>
  <div class="top-accent"></div>

  <svg class="hero-photo" viewBox="0 0 600 325" role="img" aria-label="Blue-toned photo of hands typing on a laptop with cloud graphics">
    <defs>
      <linearGradient id="heroTone" x1="0" y1="0" x2="1" y2="1">
        <stop offset="0" stop-color="#1b5db8"/>
        <stop offset="0.55" stop-color="#2f78cc"/>
        <stop offset="1" stop-color="#0b4aa0"/>
      </linearGradient>
    </defs>
    <polygon points="0,0 560,0 395,325 0,325" fill="url(#heroTone)"/>
  </svg>

  <svg class="hero-stripe" viewBox="0 0 849 460" aria-hidden="true">
    <polygon points="531,6 572,81 383,423 333,423" fill="#0e4fb0"/>
  </svg>

  <h1 class="headline">
    <span class="strong">Futuristic</span>
    <span class="light">Tech</span>
    <span class="strong">Company</span>
  </h1>

  <div class="brand-name"><span class="brand-mark"></span>Brightmoor<br>Systems</div>

  <p class="tiers-intro">We will be providing</p>
  <svg class="tiers-band" viewBox="0 0 361 64" aria-hidden="true">
    <polygon points="50,0 361,0 361,64 0,64" fill="#0677BA"/>
  </svg>
  <h2 class="tiers-title">Five Tiers:</h2>

  <div class="side-accent"></div>

  <section class="tier-row">
    <div class="tier tier-starter">
      <span class="tier-icon"><svg viewBox="0 0 40 40"><path d="M14 26 C12 16 20 8 32 8 C32 20 24 28 14 26Z"/><circle cx="24" cy="16" r="3"/><path d="M14 26 L8 24 L13 18 L18 18"/><path d="M14 26 L16 32 L22 27 L22 22"/><path d="M10 30 L6 34 M13 32 L10 35"/></svg></span>
      Starter
    </div>
    <div class="tier tier-growth">
      <span class="tier-icon"><svg viewBox="0 0 40 40"><rect x="7" y="24" width="5" height="10"/><rect x="15" y="20" width="5" height="14"/><rect x="23" y="16" width="5" height="18"/><rect x="31" y="12" width="4" height="22"/><path d="M6 18 L16 12 L22 14 L33 6 M28 6 L33 6 L33 10"/></svg></span>
      Growth
    </div>
    <div class="tier tier-professional">
      <span class="tier-icon"><svg viewBox="0 0 40 40"><circle cx="20" cy="13" r="6"/><path d="M8 36 C8 28 13 24 20 24 C27 24 32 28 32 36"/><path d="M20 24 L18 30 L20 34 L22 30 Z"/></svg></span>
      Professional
    </div>
    <div class="tier tier-premier">
      <span class="tier-icon"><svg viewBox="0 0 40 40"><circle cx="9" cy="6" r="2"/><circle cx="31" cy="6" r="2"/><path d="M9 8 V32 M31 8 V32 M5 34 H13 M27 34 H35"/><path d="M9 12 C14 20 26 20 31 12"/></svg></span>
      Premier
    </div>
    <div class="tier tier-elite">
      <span class="tier-icon"><svg viewBox="0 0 40 40"><path d="M14 4 L14 14 L20 18 L26 14 L26 4"/><path d="M20 19 L22.6 24.5 L28.5 25 L24 29 L25.4 35 L20 31.8 L14.6 35 L16 29 L11.5 25 L17.4 24.5 Z"/></svg></span>
      Elite
    </div>
  </section>

  <div class="side-accent-light"></div>

  <ul class="selling-points">
    <li>Hosted in a local Perth-based Tier3 and Tier4 datacentres</li>
    <li>WA owned hosting - support local</li>
    <li>Low latency - ultra fast local hosting</li>
    <li>Includes Quorra Host Datacentre licensing</li>
    <li>Includes WallHaven managed firewalls for enterprise level threat detection</li>
    <li>Includes all infrastructure maintenance services</li>
    <li>Full self management of VMs through customer portal</li>
    <li>Includes a 1gbps internet link</li>
    <li>Predictable fixed monthly fee with no dynamic billing</li>
    <li>No additional charges for storage transactions, internet usage, VM snapshots,<br>datacentre bandwidth usage and firewall traffic usage.</li>
    <li>Highly available cluster, no single point of failure.</li>
    <li>Pricing is based on 36 months commit</li>
    <li>Yearly rate increases capped to a maximum of Australian CPI</li>
    <li>All plans have 24/7/365 support with dedicated after hours number.</li>
    <li>Managed backup and managed disaster recovery services can be added to plans</li>
  </ul>

  <div class="footer-bar one"></div>
  <div class="footer-bar two"></div>
  <div class="footer-bar three"></div>
</main>
</body>
</html>
```